iOS7 test prep app

I need 3 basic screens and 2 product images for an iOS7 app I am prototyping. I provided lots of detail in the attached brief. This is an education product, so warm colors (especially reds) work best.

If you've done flat design for mobile products, please take a look ... Thanks!

Greetings, all. Thank you for your submissions. I am meeting with my product development team this week to review your submissions, and will select a designer before the end of the week. I appreciate your patience with my process, and thank you again for your interest in my project. I'll be back to you soon ... -Dorian

```html
<!DOCTYPE html>
<html lang="en">
<head>
<meta charset="utf-8">
<title>Test Prep — Question Screens</title>
<link href="https://fonts.googleapis.com/css2?family=Open+Sans:wght@400;600;700&display=swap" rel="stylesheet">
<style>
:root{
  --page:#eeeeec;
  --screen:#ffffff;
  --ink:#222222;
  --text:#3a3a3a;
  --line:#d6d6d6;
  --btn-top:#fbfbfb;
  --btn-bot:#c9c9cb;
  --btn-sel-top:#d4d4d4;
  --btn-sel-bot:#9d9d9f;
  --orange-top:#ff7a1c;
  --orange-bot:#f23c00;
  --gray-top:#9a9a9a;
  --gray-bot:#6b6b6b;
  --green-top:#b5e24a;
  --green-bot:#7fbe1e;
  --wrong:#c8262d;
  --blue-top:#4fb2e4;
  --blue-bot:#1478ad;
  --minus:#d9201b;
}
*{box-sizing:border-box;margin:0;padding:0}
html,body{width:1137px;height:1200px;overflow:hidden;background:var(--page);font-family:"Open Sans",Arial,sans-serif;color:var(--ink)}
.screen{position:absolute;top:202px;width:397px;height:804px;background:var(--screen);box-shadow:0 2px 12px rgba(0,0,0,.12)}
.screen--ask{left:102px}
.screen--result{left:633px}
.topbar{position:absolute;left:0;top:0;width:100%;height:56px;background:linear-gradient(#ffffff,#f2f2f2);border-bottom:1px solid var(--line)}
.topbar__menu{position:absolute;left:22px;top:20px}
.topbar__title{position:absolute;left:0;right:0;top:17px;text-align:center;font-weight:700;font-size:16.5px;letter-spacing:.1px}
.question{position:absolute;left:23px;top:82px;width:354px;height:202px;border:1px solid #dcdcdc;border-radius:4px;background:linear-gradient(#ffffff,#f6f6f6)}
.question__icon{position:absolute;left:11px;top:82px}
.question__text{position:absolute;left:62px;top:20px;width:280px;font-size:16px;line-height:28px;color:var(--text)}
.answer{position:absolute;left:23px;width:354px;height:47px;border:1px solid #c4c4c4;border-radius:4px;background:linear-gradient(var(--btn-top) 0%,#ececec 48%,#d9d9db 52%,var(--btn-bot) 100%);font-weight:700;font-size:15.5px;line-height:45px;padding-left:17px;color:#333;text-shadow:0 1px 0 rgba(255,255,255,.7)}
.answer--a{top:298px}.answer--b{top:361px}.answer--c{top:425px}.answer--d{top:489px}
.answer--selected{background:linear-gradient(#c6c6c6,#b0b0b2 50%,var(--btn-sel-bot));box-shadow:inset 0 2px 5px rgba(0,0,0,.25)}
.answer--correct{background:linear-gradient(var(--green-top),#9fd23a 50%,var(--green-bot));border-color:#72a81c;color:#2b3a0c;text-shadow:0 1px 0 rgba(255,255,255,.35)}
.answer__mark{position:absolute;right:11px;top:12px}
.pill{position:absolute;height:49px;border-radius:3px;color:#fff;font-weight:700;font-size:16.5px;text-align:center;line-height:49px;text-shadow:0 -1px 0 rgba(0,0,0,.25)}
.pill--orange{background:linear-gradient(var(--orange-top),var(--orange-bot));border:1px solid #d83400}
.pill--gray{background:linear-gradient(var(--gray-top),var(--gray-bot));border:1px solid #5e5e5e}
.confidence{left:114px;top:564px;width:167px}
.submit{left:113px;top:726px;width:170px;height:51px;line-height:51px}
.slider{position:absolute;left:0;top:650px;width:100%;height:44px}
.slider__track{position:absolute;left:83px;top:17px;width:234px;height:10px;border-radius:5px;background:linear-gradient(#c9c9c9,#e2e2e2);box-shadow:inset 0 1px 2px rgba(0,0,0,.2)}
.slider__fill{position:absolute;left:0;top:0;width:151px;height:10px;border-radius:5px;background:linear-gradient(var(--orange-top),var(--orange-bot))}
.slider__knob{position:absolute;left:141px;top:-6px;width:22px;height:22px;border-radius:50%;background:radial-gradient(circle at 50% 40%,#ffffff,#dcdcd8);box-shadow:0 1px 3px rgba(0,0,0,.35)}
.slider__btn{position:absolute;top:2px}
.slider__btn--minus{left:23px}
.slider__btn--plus{left:334px}
.explain{position:absolute;left:23px;top:553px;width:354px;height:152px;border:1px solid #dcdcdc;border-radius:4px;background:linear-gradient(#ffffff,#f6f6f6);padding:14px 17px;font-size:15.5px;line-height:25px;color:var(--text)}
.explain strong{color:var(--ink)}
.save{left:23px;top:725px;width:167px}
.next{left:207px;top:724px;width:170px;height:51px;line-height:51px}
</style>
</head>
<body>

<svg width="0" height="0" style="position:absolute">
  <defs>
    <linearGradient id="qGrad" x1="0" y1="0" x2="0" y2="1"><stop offset="0" stop-color="#5cc0ec"/><stop offset="1" stop-color="#0f6e9f"/></linearGradient>
    <linearGradient id="blueGrad" x1="0" y1="0" x2="0" y2="1"><stop offset="0" stop-color="#4fb2e4"/><stop offset="1" stop-color="#1478ad"/></linearGradient>
    <linearGradient id="redGrad" x1="0" y1="0" x2="0" y2="1"><stop offset="0" stop-color="#ee3a2f"/><stop offset="1" stop-color="#b8140f"/></linearGradient>
    <symbol id="menuIcon" viewBox="0 0 32 16"><rect y="0" width="32" height="2.6" fill="#333"/><rect y="6.7" width="32" height="2.6" fill="#333"/><rect y="13.4" width="32" height="2.6" fill="#333"/></symbol>
    <symbol id="helpIcon" viewBox="0 0 38 38"><circle cx="19" cy="19" r="18" fill="url(#qGrad)" stroke="#0b5c86" stroke-width="1"/><text x="19" y="27" text-anchor="middle" font-family="Open Sans,Arial,sans-serif" font-weight="700" font-size="24" fill="#fff">?</text></symbol>
    <symbol id="wrongIcon" viewBox="0 0 22 22"><circle cx="11" cy="11" r="9.5" fill="#fff" stroke="#c8262d" stroke-width="2"/><path d="M7.5 7.5l7 7M14.5 7.5l-7 7" stroke="#c8262d" stroke-width="2.2" stroke-linecap="round"/></symbol>
    <symbol id="rightIcon" viewBox="0 0 22 22"><circle cx="11" cy="11" r="9.5" fill="none" stroke="#3f5e10" stroke-width="1.6"/><path d="M6.8 11.3l2.9 2.9 5.6-6" fill="none" stroke="#3f5e10" stroke-width="1.8" stroke-linecap="round" stroke-linejoin="round"/></symbol>
  </defs>
</svg>

<section class="screen screen--ask">
  <header class="topbar">
    <svg class="topbar__menu" width="32" height="16"><use href="#menuIcon"/></svg>
    <h1 class="topbar__title">QUESTION 7 OF 100</h1>
  </header>
  <div class="question">
    <svg class="question__icon" width="38" height="38"><use href="#helpIcon"/></svg>
    <p class="question__text">A patient presents to the emergency room with the following symptoms: Anxiety, dyspnea, rhonchi, fever, Oxygen saturation of 88%, and a pH of 7.21. The nurse realized that the patient suffering from:</p>
  </div>
  <div class="answer answer--a">A. RESPIRATORY ALKALOSIS</div>
  <div class="answer answer--b">B. METABOLIC ALKALOSIS</div>
  <div class="answer answer--c answer--selected">C. RESPIRATORY ACIDOSIS</div>
  <div class="answer answer--d">D. METABOLIC ACIDOSIS</div>
  <div class="pill pill--orange confidence">CONFIDENCE</div>
  <div class="slider">
    <svg class="slider__btn slider__btn--minus" width="40" height="40" viewBox="0 0 40 40"><circle cx="20" cy="20" r="19" fill="#e4e4e4"/><circle cx="20" cy="20" r="15" fill="url(#redGrad)"/><rect x="14" y="18.6" width="12" height="2.8" fill="#fff"/></svg>
    <div class="slider__track"><div class="slider__fill"></div><div class="slider__knob"></div></div>
    <svg class="slider__btn slider__btn--plus" width="40" height="40" viewBox="0 0 40 40"><circle cx="20" cy="20" r="19" fill="#e4e4e4"/><circle cx="20" cy="20" r="15" fill="url(#blueGrad)"/><rect x="14" y="18.6" width="12" height="2.8" fill="#fff"/><rect x="18.6" y="14" width="2.8" height="12" fill="#fff"/></svg>
  </div>
  <div class="pill pill--gray submit">SUBMIT</div>
</section>

<section class="screen screen--result">
  <header class="topbar">
    <svg class="topbar__menu" width="32" height="16"><use href="#menuIcon"/></svg>
    <h1 class="topbar__title">QUESTION 7 OF 100</h1>
  </header>
  <div class="question">
    <svg class="question__icon" width="38" height="38"><use href="#helpIcon"/></svg>
    <p class="question__text">A patient presents to the emergency room with the following symptoms: Anxiety, dyspnea, rhonchi, fever, Oxygen saturation of 88%, and a pH of 7.21. The nurse realized that the patient suffering from:</p>
  </div>
  <div class="answer answer--a">A. RESPIRATORY ALKALOSIS<svg class="answer__mark" width="22" height="22"><use href="#wrongIcon"/></svg></div>
  <div class="answer answer--b">B. METABOLIC ALKALOSIS<svg class="answer__mark" width="22" height="22"><use href="#wrongIcon"/></svg></div>
  <div class="answer answer--c answer--correct">C. RESPIRATORY ACIDOSIS<svg class="answer__mark" width="22" height="22"><use href="#rightIcon"/></svg></div>
  <div class="answer answer--d">D. METABOLIC ACIDOSIS<svg class="answer__mark" width="22" height="22"><use href="#wrongIcon"/></svg></div>
  <div class="explain"><strong>The correct answer is C.</strong> A key symptom of respiratory distress syndrome is the inability of the respiratory system to exchange gases, resulting in respiratory. acidosis.</div>
  <div class="pill pill--orange save">SAVE &amp; CLOSE</div>
  <div class="pill pill--gray next">NEXT QUESTION</div>
</section>

</body>
</html>
```